Small Business Broker Business Card Design

A business card design for a small business brokerage, which is a financial service, not unlike real estate brokerage, but for small businesses such as laundromats, pizza shops, restaurants, cleaners etc. The designs should all be simple, more conservative in nature, using the colors and font of the logo. Again, think real estate Brokerage as a business context
Contact Information for Business Card
Name: Dale R. Whitmore. Title: Small Business Advisor. Email: d.whitmore@lanternbridgeadvisory.com. Mobile: (917) 555-0148. Office: (718) 555-0193. www.lanternbridgeadvisory.com

```html
<!DOCTYPE html>
<html lang="en">
<head>
<meta charset="utf-8">
<title>Lantern Bridge Advisory — Business Card</title>
<link rel="stylesheet" href="https://fonts.googleapis.com/css2?family=Montserrat:wght@400;500;700&display=swap">
<style>
  :root {
    --navy: #1d3a78;
    --green: #8cc63f;
    --green-light: #9ed14f;
    --paper: #ffffff;
    --text: #1f2a44;
    --stage: #e9e9e6;
  }
  * { box-sizing: border-box; margin: 0; padding: 0; }
  html, body {
    width: 1200px; height: 786px; overflow: hidden;
    background: var(--stage);
    font-family: "Montserrat", sans-serif;
  }
  .canvas { position: relative; width: 1200px; height: 786px; }
  .card {
    position: absolute; top: 245px;
    width: 520px; height: 297px;
    box-shadow: 0 10px 24px rgba(0,0,0,0.18);
    overflow: hidden;
  }
  .card--front { left: 50px; background: var(--paper); }
  .card--back { left: 630px; background: var(--green); }

  .brand { position: absolute; white-space: nowrap; }
  .brand__row { display: flex; align-items: center; gap: 9px; }
  .brand__dot { flex: none; width: 13px; height: 13px; border-radius: 50%; background: var(--navy); }
  .brand__name {
    font-weight: 700; color: var(--navy);
    text-transform: uppercase; letter-spacing: 0.4px;
  }
  .brand__tagline {
    font-weight: 500; text-transform: uppercase; letter-spacing: 1.5px;
  }

  .card--front .brand { right: 40px; top: 92px; }
  .card--front .brand__name { font-size: 20px; }
  .card--front .brand__tagline { color: var(--green); font-size: 9px; margin-top: 4px; margin-left: 22px; }

  .back-texture {
    position: absolute; inset: 0;
    background: linear-gradient(160deg, var(--green-light) 0%, var(--green) 55%);
  }
  .card--back .brand { left: 50%; top: 50%; transform: translate(-50%, -50%); }
  .card--back .brand__name { font-size: 18px; }
  .card--back .brand__tagline { color: var(--paper); font-size: 8.4px; margin-top: 4px; margin-left: 22px; }

  .person { position: absolute; left: 30px; top: 166px; white-space: nowrap; }
  .person__name { font-size: 22px; font-weight: 700; color: var(--navy); line-height: 26px; }
  .person__title { font-size: 12px; font-weight: 500; color: var(--text); margin-top: 1px; }

  .rule {
    position: absolute; left: 248px; right: 40px; top: 190px;
    height: 1px; background: var(--green);
  }

  .online { position: absolute; right: 32px; top: 200px; text-align: right; }
  .phones { position: absolute; left: 32px; top: 232px; }
  .contact-line {
    display: flex; align-items: center; gap: 8px; white-space: nowrap;
    font-size: 11.5px; color: var(--text); line-height: 19px;
  }
  .online .contact-line { justify-content: flex-end; }
  .phones .contact-line { font-size: 13px; line-height: 22px; }
  .icon { width: 11px; height: 11px; fill: var(--navy); flex: none; }

  .band { position: absolute; bottom: 0; height: 14px; }
  .band--green { left: 0; width: 300px; background: var(--green); }
  .band--navy { left: 300px; right: 0; background: var(--navy); }
</style>
</head>
<body>
<main class="canvas">

  <section class="card card--front" aria-label="Business card front">
    <div class="brand">
      <div class="brand__row">
        <span class="brand__dot"></span>
        <span class="brand__name">Lantern Bridge Advisory, Inc</span>
      </div>
      <div class="brand__tagline">Trusted guidance to buy or sell a shop nearby</div>
    </div>

    <div class="person">
      <div class="person__name">Dale R. Whitmore</div>
      <div class="person__title">Small Business Advisor</div>
    </div>
    <div class="rule"></div>

    <div class="online">
      <div class="contact-line">d.whitmore@lanternbridgeadvisory.com
        <svg class="icon" viewBox="0 0 12 12"><path d="M0 2h12v8H0z M0 2l6 4 6-4" fill="var(--navy)" stroke="#fff" stroke-width="0.8"/></svg>
      </div>
      <div class="contact-line">www.lanternbridgeadvisory.com
        <svg class="icon" viewBox="0 0 12 12"><circle cx="6" cy="6" r="5.5"/><path d="M0.5 6h11M6 0.5c-2.5 3-2.5 8 0 11M6 0.5c2.5 3 2.5 8 0 11" stroke="#fff" stroke-width="0.8" fill="none"/></svg>
      </div>
    </div>

    <div class="phones">
      <div class="contact-line">
        <svg class="icon" viewBox="0 0 12 12"><path d="M1 4c0-1.5 2-2.5 5-2.5s5 1 5 2.5v1H8.5V4h-5v1H1z M3 6h6l1.5 4h-9z"/></svg>
        (718) 555-0193
      </div>
      <div class="contact-line">
        <svg class="icon" viewBox="0 0 12 12"><path d="M2.5 1l2 2.5-1.2 1.3c.6 1.4 1.8 2.6 3.2 3.2L7.8 6.8 10.5 8.5 9.5 11C5 10.5 1.5 7 1 2.5z"/></svg>
        (917) 555-0148
      </div>
    </div>

    <div class="band band--green"></div>
    <div class="band band--navy"></div>
  </section>

  <section class="card card--back" aria-label="Business card back">
    <div class="back-texture" role="img" aria-label="Subtle tone-on-tone chevron pattern across the green back"></div>
    <div class="brand">
      <div class="brand__row">
        <span class="brand__dot"></span>
        <span class="brand__name">Lantern Bridge Advisory, Inc</span>
      </div>
      <div class="brand__tagline">Trusted guidance to buy or sell a shop nearby</div>
    </div>
  </section>

</main>
</body>
</html>
```